Flyer Design

I need a nice professional flyer design to use for advertising my lawn/snow removal business. Flyers I am using are 5.47"x4.21". I've attached a flyer I found online that I liked. Just wanting something creative and professional. The images of the logos I attached are of the original logo design, and the new color design we are using. There is also a mockup of our tshirt design to give you an idea of the actual color on the tshirt, since the jpeg logo isn't exactly accurate on color.
Things I need on the flyer in no particular order:
"Snow is coming"
"Don't Wait Until It's TOO LATE!"
"Free Estimates"
Services offered
"Commercial/Residential"
"Snow Plowing"
"Snow Blowing"
"Snow Shoveling"
"Ice Removal"
"Salting/Sanding"
"Fully Licensed and Insured"
"Available and ON CALL 24/7"
"Seasonal Packages Available"
"CALL NOW TO RESERVE"

```html
<!DOCTYPE html>
<html lang="en">
<head>
<meta charset="utf-8">
<title>Snow Is Coming – Snow Removal Flyer</title>
<link rel="stylesheet" href="https://fonts.googleapis.com/css2?family=Jost:wght@700;800&family=Alfa+Slab+One&family=Oswald:wght@300;400&family=Arimo:wght@400&display=swap">
<style>
  :root {
    --sky-top: #1b4f9c;
    --sky-mid: #2f8cc4;
    --sky-low: #8ed6ee;
    --snow: #ffffff;
    --snow-shade: #dcedf8;
    --snow-deep: #c6e2f3;
    --headline-yellow: #fff200;
    --title-blue: #b9e6f6;
    --packages-blue: #1a4f93;
    --badge-blue: #1690c8;
    --cta-orange: #f7941d;
    --ink: #1a1a1a;
    --plow-grey: #a7a9ac;
    --plow-orange: #f58a1f;
  }
  html, body {
    margin: 0;
    padding: 0;
    width: 923px;
    height: 1200px;
    overflow: hidden;
    background: var(--snow);
  }
  .flyer {
    position: relative;
    width: 923px;
    height: 1200px;
    overflow: hidden;
  }
  .backdrop {
    position: absolute;
    inset: 0;
  }
  .headline {
    position: absolute;
    top: 20px;
    left: 0;
    width: 100%;
    margin: 0;
    text-align: center;
    font-family: "Jost", sans-serif;
    font-weight: 800;
    font-size: 55px;
    line-height: 1;
    color: var(--headline-yellow);
  }
  .title {
    position: absolute;
    top: 84px;
    left: 0;
    width: 100%;
    margin: 0;
    text-align: center;
    font-family: "Alfa Slab One", serif;
    font-weight: 400;
    font-size: 72px;
    line-height: 1;
    color: var(--title-blue);
  }
  .services {
    position: absolute;
    top: 168px;
    left: 0;
    width: 100%;
    margin: 0;
    padding: 0;
    list-style: none;
    text-align: center;
    font-family: "Oswald", sans-serif;
    font-weight: 300;
    font-size: 29px;
    line-height: 39px;
    color: var(--snow);
  }
  .packages {
    position: absolute;
    top: 409px;
    left: 0;
    width: 100%;
    margin: 0;
    text-align: center;
    font-family: "Alfa Slab One", serif;
    font-size: 23px;
    line-height: 1.2;
    letter-spacing: 0.8px;
    color: var(--packages-blue);
  }
  .plow-scene {
    position: absolute;
    left: 70px;
    top: 440px;
  }
  .estimate-badge {
    position: absolute;
    left: 30px;
    top: 795px;
    width: 236px;
    height: 236px;
  }
  .estimate-badge span {
    position: absolute;
    inset: 0;
    display: flex;
    align-items: center;
    justify-content: center;
    text-align: center;
    font-family: "Jost", sans-serif;
    font-weight: 700;
    font-size: 31px;
    line-height: 1.1;
    color: var(--snow);
    transform: rotate(-18deg);
  }
  .availability {
    position: absolute;
    top: 1062px;
    left: 0;
    width: 100%;
    margin: 0;
    text-align: center;
    font-family: "Alfa Slab One", serif;
    font-size: 43px;
    line-height: 1;
    color: var(--ink);
  }
  .call-to-action {
    position: absolute;
    top: 1110px;
    left: 0;
    width: 100%;
    margin: 0;
    text-align: center;
    font-family: "Jost", sans-serif;
    font-weight: 700;
    font-size: 68px;
    line-height: 1;
    letter-spacing: 1px;
    color: var(--cta-orange);
  }
  .credentials {
    position: absolute;
    top: 1173px;
    left: 0;
    width: 100%;
    margin: 0;
    text-align: center;
    font-family: "Arimo", sans-serif;
    font-size: 19px;
    line-height: 1;
    color: var(--ink);
  }
</style>
</head>
<body>
<main class="flyer">
  <svg class="backdrop" width="923" height="1200" viewBox="0 0 923 1200" aria-hidden="true">
    <defs>
      <linearGradient id="sky" x1="0" y1="0" x2="0" y2="1">
        <stop offset="0" stop-color="var(--sky-top)"/>
        <stop offset="0.45" stop-color="var(--sky-mid)"/>
        <stop offset="1" stop-color="var(--sky-low)"/>
      </linearGradient>
      <linearGradient id="hill" x1="0" y1="0" x2="0" y2="1">
        <stop offset="0" stop-color="var(--snow-shade)"/>
        <stop offset="1" stop-color="var(--snow)"/>
      </linearGradient>
    </defs>
    <rect width="923" height="760" fill="url(#sky)"/>
    <path d="M470 780 Q560 600 700 545 Q800 515 923 530 L923 780 Z" fill="var(--snow-deep)"/>
    <path d="M0 690 Q400 600 923 720 L923 1200 L0 1200 Z" fill="url(#hill)"/>
    <path d="M0 860 Q500 760 923 880 L923 1200 L0 1200 Z" fill="var(--snow-shade)" opacity="0.5"/>
    <path d="M200 1200 Q520 900 923 880 L923 1200 Z" fill="var(--snow)"/>
  </svg>

  <h1 class="headline">Don't Wait Till It's TOO LATE!</h1>
  <h2 class="title">Snow is coming</h2>

  <ul class="services">
    <li>Commercial/Residential</li>
    <li>Snow Plowing</li>
    <li>Snow Blowing</li>
    <li>Snow Shoveling</li>
    <li>Ice Removal</li>
    <li>Salting/Sanding</li>
  </ul>
  <p class="packages">Seasonal Packages Available</p>

  <svg class="plow-scene" width="780" height="390" viewBox="0 0 780 390" role="img" aria-label="Illustration of an orange snow plow truck pushing snow over snowy hills, with playful snowballs and a snowman nearby">
    <defs>
      <radialGradient id="scene-tone" cx="0.5" cy="0.5" r="0.5">
        <stop offset="0" stop-color="var(--plow-orange)" stop-opacity="0.7"/>
        <stop offset="0.35" stop-color="var(--plow-grey)" stop-opacity="0.45"/>
        <stop offset="0.7" stop-color="var(--snow)" stop-opacity="0.4"/>
        <stop offset="1" stop-color="var(--snow)" stop-opacity="0"/>
      </radialGradient>
    </defs>
    <ellipse cx="330" cy="180" rx="320" ry="180" fill="url(#scene-tone)"/>
  </svg>

  <div class="estimate-badge">
    <svg width="236" height="236" viewBox="0 0 236 236" aria-hidden="true">
      <polygon fill="var(--badge-blue)" points="118,4 136,36 167,14 172,51 209,43 197,79 232,92 204,118 232,144 197,157 209,193 172,185 167,222 136,200 118,232 100,200 69,222 64,185 27,193 39,157 4,144 32,118 4,92 39,79 27,43 64,51 69,14 100,36"/>
    </svg>
    <span>Free<br>Estimates!</span>
  </div>

  <p class="availability">Available and ON CALL 24/7</p>
  <p class="call-to-action">CALL NOW TO RESERVE</p>
  <p class="credentials">Fully Licensed and Insured*</p>
</main>
</body>
</html>
```